Adventurous female pilot

I am looking for a personal business card, for a very well qualified female pilot, with a lot of aviation experience.

Currently an airline pilot, have worked as a bush pilot in Africa, looking to get into corporate aviation, or private jet owners.
Want a classy looking card for networking...

Could be interested in a retro\vintage look also?!

An idea,, is an african sunset background, with my wings\logo on it
Updates

I just want to say thank you to all of your for your amazing designs!

I have been very busy flying this past week , so not had a chance to be on the computer much.
But I provide some feedback, and conclusions very soon!
Thank you again.

Marla

Reason: Still waiting on a couple of revisions to be 100% about my choice!

Target Market(s)

corporate aviation, private jet owners, casino's,
General audience.
networking

Industry/Entity Type

Airline

Requirements
Nice to have
• Classy, edgy, sexy, but also feminine

```html
<!DOCTYPE html>
<html lang="en">
<head>
<meta charset="utf-8">
<title>Marla Hallett – Business Cards</title>
<link rel="stylesheet" href="https://fonts.googleapis.com/css2?family=Arimo:wght@400;500&family=Pacifico&display=swap">
<style>
  :root {
    --canvas: #ffffff;
    --ink: #111111;
    --card-white: #ffffff;
    --gold: #e9a62a;
    --gold-spot: #d48b1c;
    --amber: #c98d22;
    --amber-spot: #6e4b14;
    --pink: #ff6e9b;
    --pink-spot: #f58bb6;
    --pink-deep: #ee6699;
    --mark: #555555;
  }
  * { margin: 0; padding: 0; box-sizing: border-box; }
  html, body { width: 1200px; height: 834px; overflow: hidden; background: var(--canvas); }
  .sheet { position: relative; width: 1200px; height: 834px; }

  .card {
    position: absolute;
    width: 527px;
    height: 335px;
    border-radius: 18px;
    overflow: hidden;
    background: var(--card-white);
  }
  .card--outlined { border: 2px solid var(--ink); }
  .card--gold { left: 58px; top: 55px; }
  .card--pink { left: 619px; top: 63px; background: var(--pink); border-radius: 20px; }
  .card--amber { left: 55px; top: 441px; }
  .card--pink-spotted { left: 617px; top: 422px; border-radius: 20px; }

  .pattern-band { position: absolute; left: 0; right: 0; }
  .pattern-band--top { top: 0; height: 46px; }
  .pattern-band--bottom { bottom: 0; height: 38px; }
  .pattern-band--gold { background: linear-gradient(100deg, var(--gold), var(--gold-spot) 50%, var(--gold)); }
  .pattern-band--amber { background: linear-gradient(100deg, var(--amber), var(--amber-spot) 50%, var(--amber)); }
  .pattern-fill {
    position: absolute; inset: 0;
    background: linear-gradient(120deg, var(--pink-deep), var(--pink-spot) 50%, var(--pink-deep));
  }

  .card__name {
    position: absolute;
    left: 18px;
    top: 44px;
    font-family: "Pacifico", cursive;
    font-size: 66px;
    line-height: 1.2;
    color: var(--ink);
    white-space: nowrap;
  }
  .card--pink .card__name, .card--pink-spotted .card__name { left: 0; top: 30px; }

  .card__contact {
    position: absolute;
    left: 170px;
    top: 210px;
    font-family: "Arimo", Arial, sans-serif;
    font-weight: 500;
    font-size: 21px;
    line-height: 29px;
    color: var(--ink);
    white-space: nowrap;
  }
  .card--pink .card__contact, .card--pink-spotted .card__contact { left: 140px; top: 226px; }

  .card__mark {
    position: absolute;
    left: 8px;
    top: 218px;
    width: 140px;
    display: flex;
    flex-direction: column;
    align-items: center;
    gap: 6px;
    font-family: "Arimo", Arial, sans-serif;
    font-weight: 400;
    font-size: 9px;
    letter-spacing: 0.5px;
    text-align: center;
    color: var(--mark);
  }
  .card--pink .card__mark, .card--pink-spotted .card__mark { left: -16px; top: 232px; }
  .card__mark-dot { width: 30px; height: 30px; border-radius: 50%; border: 1.5px solid var(--mark); }
</style>
</head>
<body>
<main class="sheet">

  <section class="card card--outlined card--gold">
    <div class="pattern-band pattern-band--top pattern-band--gold" role="img" aria-label="Gold leopard print pattern band"></div>
    <div class="pattern-band pattern-band--bottom pattern-band--gold" role="img" aria-label="Gold leopard print pattern band"></div>
    <h1 class="card__name">Marla Hallett</h1>
    <div class="card__mark"><span class="card__mark-dot"></span><span>MARLA HALLETT<br>AVIATION</span></div>
    <p class="card__contact">Email: marlahallett@mail.com<br>Cell US: +1 702-555-0143<br>Cell Taipei: +886 970-555-214</p>
  </section>

  <section class="card card--pink">
    <h1 class="card__name">Marla Hallett</h1>
    <div class="card__mark"><span class="card__mark-dot"></span><span>MARLA HALLETT<br>AVIATION</span></div>
    <p class="card__contact">Email: marlahallett@mail.com<br>Cell US: +1 702-555-0143<br>Cell Taipei: +886 970-555-214</p>
  </section>

  <section class="card card--outlined card--amber">
    <div class="pattern-band pattern-band--top pattern-band--amber" role="img" aria-label="Amber and brown leopard print pattern band"></div>
    <div class="pattern-band pattern-band--bottom pattern-band--amber" role="img" aria-label="Amber and brown leopard print pattern band"></div>
    <h1 class="card__name">Marla Hallett</h1>
    <div class="card__mark"><span class="card__mark-dot"></span><span>MARLA HALLETT<br>AVIATION</span></div>
    <p class="card__contact">Email: marlahallett@mail.com<br>Cell US: +1 702-555-0143<br>Cell Taipei: +886 970-555-214</p>
  </section>

  <section class="card card--pink-spotted">
    <div class="pattern-fill" role="img" aria-label="Pink leopard print pattern background"></div>
    <h1 class="card__name">Marla Hallett</h1>
    <div class="card__mark"><span class="card__mark-dot"></span><span>MARLA HALLETT<br>AVIATION</span></div>
    <p class="card__contact">Email: marlahallett@mail.com<br>Cell US: +1 702-555-0143<br>Cell Taipei: +886 970-555-214</p>
  </section>

</main>
</body>
</html>
```